Wordpress Theme for Medical Clinics

** Please view updated Sitemap2.pdf doc to clarify some confusion ***

This is a multiuser WordPress subscription site for medical clinics. Please see attachment for sitemap. Please do not include extra content like social media icons, search bars, or images. If you have questions, please ask for clarification.
The site contains the following pages and sub-pages:

1. Home
2. Our Clinic
2a. Our Clinic > Mission
2b. Our Clinic > Services
2c. Our Clinic > Clinic Policies
2d. Our Clinic > Schedules
3. Our Staff
3a. Our Staff > [Staff member page]
4. Resources
4a. Resources > Patient Health (index)
4b. Resources > Patient Health (index) > [post]
4c. Resources > Links
4d. Resources > Forms
5. Alerts
5a. Alerts > [Alert Page]
6. Contact Us

Includes the Following Pages, Subpages, and Content
1. Home
a. About Us
b. Our Staff
c. Bulletins
d. Accepting New Patients (shown as an alert widget)
e. Links
i. Physician Toolbox
ii. Book an Appointment
f. Clinic Policies
i. Show first 3 policies (e.g. Late Arrivals, Missed Appointments, Fees)
ii. Link to Clinic Policies page
g. Primary widget (displayed on all pages)
i. Hours of operation
ii. Contact Info
1. Tel
2. Fax
3. Email
4. Address
5. Get directions (link to Google Maps)
2. Our Clinic
a. Main Page
i. Clinic Name
ii. Overview
iii. Languages Spoken
iv. Secondary Navigation
1. Mission
2. Services
3. Clinic Policies
4. Schedules (see attachment)
b. Our Clinic > Mission
c. Our Clinic > Services
i. For each service include service TITLE and DESCRIPTION
d. Our Clinic > Clinic Policies
i. For each policy include policy TITLE and DESCRIPTION
ii. Include the following policies in mockup
1. Late arrivals
2. Missed appointments
3. Fees for missed appointments
4. Referrals and follow-ups
5. Services not covered by RDV
6. Information for TQL patients
7. Medical Legal Reports
e. Our Clinic > Schedules
3. Our Staff
a. Main Page
i. Display a list of staff members. Include NAME and DESIGNATION
b. Our Staff > [Staff Name]
i. Include NAME, PICTURE, DESIGNATION, and BIO
4. Resources
a. Resources > Patient Health
i. Main Page
1. Posts (ordered by date)
a. Title
b. Summary
2. Side Navigation
a. Post Categories
ii. Patient Health > [post title]
1. Title
2. Post Category
3. Date
4. Author
5. Summary
6. Body
b. Resources > Links
1. Secondary Navigation - Categories
a. Sample Categories:
i. Local Services
ii. RDV and Drug Coverage
iii. Mental Health Resources
2. Category page
a. Include the following links in the 'Local Services' category
i. Hypertension clinics
ii. Home Care services
iii. Vaccine Clinics
c. Resources > Forms
i. Display a table with form TITLE and CATEGORY
ii. Side Navigation
1. Form Categories
a. Use the following sample Categories
i. Referrals
ii. Insurance
iii. Intake
iv. Discharge
v. Waivers
5. Alerts
a. Main page
i. List of all Alert posts
1. Include post TITLE as a link to the post
ii. Side Navigation
1. Alerts Archive
a. shown as Month + Number of posts
iii. Alerts > [Alert page]
1. Include TITLE, DATE, AUTHOR, BODY
6. Contact Us
a. Map
b. Hours of operation
c. Address
d. Phone number
e. Fax number
e. Fax number
f. Map
g. Email

Design notes:
- fixed width
- responsive (need designs for mobile, tablet, and desktop)
- simple, dark font, white background
- use Font Awesome icons where needed
- user adds own logo

Target Market(s)

Medical Clinics

Industry/Entity Type

Medical

Number of Pages Required

5+ page

Font styles to use
Serif
Sans Serif

Requirements
Must have
• Please keep designs very simple.
• Examples:
• https://www.quandrix.com/install
• http://www.tervolane.com/company/about-us
• http://brightnumberhub.org/
• http://www.vorn.com/
Should not have
• Minimal or no use of shadows and gradients

```html
<!DOCTYPE html>
<html lang="en">
<head>
<meta charset="utf-8">
<title>TQL Care Centre – Mission</title>
<link rel="stylesheet" href="https://fonts.googleapis.com/css2?family=Lato:ital,wght@0,400;0,700;1,400&display=swap">
<style>
:root{
  --page:#f3f3f3;
  --white:#ffffff;
  --accent:#4ab8d8;
  --accent-dark:#2a9fc2;
  --ink:#222222;
  --text:#555555;
  --muted:#888888;
  --rule:#e2e2e2;
  --row-alt:#ececec;
  --faint:#cfd8dc;
}
*{box-sizing:border-box;margin:0;padding:0}
html,body{width:1200px;height:975px;overflow:hidden}
body{background:var(--page);font-family:"Lato",Arial,sans-serif;color:var(--text);position:relative}
a{text-decoration:none;color:inherit}
.abs{position:absolute}

/* top bar */
.topbar{top:12px;left:155px;width:890px;height:16px;font-size:12px}
.topbar .phone{position:absolute;left:0;top:0;color:var(--text);display:flex;align-items:center;gap:7px}
.topbar .mail{position:absolute;left:104px;top:-2px;padding-left:14px;border-left:1px solid #ccc;color:var(--accent)}
.topbar .links{position:absolute;right:0;top:-2px;color:var(--accent);display:flex}
.topbar .links a{padding:0 0 0 16px}
.topbar .links a+a{margin-left:16px;border-left:1px solid #ccc}

/* card */
.card{top:38px;left:151px;width:900px;height:631px;background:var(--white)}
.header{height:79px;border-bottom:1px solid var(--rule);position:relative}
.brand{position:absolute;left:58px;top:18px}
.brand .name{display:flex;align-items:center;gap:9px;font-weight:400;font-size:18px;color:var(--ink)}
.brand .mark{width:11px;height:11px;background:var(--accent-dark)}
.brand .tag{font-style:italic;font-size:10.5px;color:var(--muted);margin-top:3px}
.nav{position:absolute;right:90px;top:21px;display:flex;font-size:10.5px;color:var(--ink);text-transform:uppercase}
.nav a{height:28px;line-height:30px;padding:0 14px}
.nav a.current{background:var(--accent);color:var(--white);border-top:3px solid var(--accent-dark);line-height:25px;border-radius:2px}

.title-band{top:117px;left:195px;width:807px;height:38px;background:var(--accent);color:var(--white);font-size:18px;font-weight:700;padding:9px 0 0 33px}

.subnav{top:162px;left:190px;width:146px;border-right:2px solid var(--accent)}
.subnav li{list-style:none;height:44px;display:flex;border-bottom:1px solid var(--rule);font-size:11px;color:var(--accent)}
.subnav .caret{width:34px;background:var(--row-alt);display:flex;align-items:center;justify-content:center}
.subnav .label{display:flex;align-items:center;padding-left:12px}
.subnav li.active{background:var(--row-alt);color:var(--ink)}

.hero{top:162px;left:345px;width:377px;height:225px;background:var(--accent);box-shadow:0 8px 10px -6px rgba(0,0,0,.18)}
.hero h2{position:absolute;left:17px;top:150px;color:var(--white);font-size:15px;font-weight:700}
.hero .btn{position:absolute;left:15px;top:177px;background:#eef7fa;color:var(--ink);font-size:15px;padding:8px 16px}

.lead{top:402px;left:347px;width:370px;font-style:italic;color:var(--accent-dark);font-size:14px;line-height:24px}
.body-copy{left:345px;width:380px;font-size:10.5px;line-height:18px;color:var(--muted);white-space:nowrap}

.hours{top:161px;left:742px;width:262px;height:332px;background:var(--page);border-bottom:3px solid var(--accent)}
.hours .head{height:38px;background:var(--accent);color:var(--white);font-weight:700;font-size:12px;display:flex;align-items:center;gap:8px;padding-left:14px}
.hours table{margin:22px 0 0 8px;width:246px;border-collapse:collapse;font-size:9.5px}
.hours td{height:30px;padding-left:14px;background:var(--white)}
.hours tr:nth-child(even) td{background:var(--row-alt)}
.hours td:first-child{font-weight:700;color:var(--text);width:108px}
.hours .holiday{display:inline-block;margin:20px 0 0 22px;font-size:10px;border-bottom:1px solid #aaa;color:var(--text)}

.contact{top:512px;left:740px;width:262px;height:128px;background:var(--accent);color:var(--white);padding:13px 12px}
.contact h3{font-size:15px;font-weight:400;color:var(--ink);display:flex;align-items:center;gap:8px;margin-bottom:6px}
.contact dl{display:grid;grid-template-columns:108px 1fr;font-size:9.5px;line-height:15px}
.contact dt{font-weight:700}

/* footer */
.fcol{top:690px}
.fcol h4{font-size:14px;font-weight:700;color:#666;text-transform:uppercase;padding-bottom:4px;border-bottom:1px solid #ddd;display:inline-block;margin-bottom:18px}
.flinks li{list-style:none;font-size:10.5px;height:22.5px;display:flex;align-items:center;gap:10px;color:var(--text)}
.flinks li.on{color:var(--accent)}
.fbig{font-size:13px;font-weight:700;color:#666;line-height:22.5px}
.fhours{font-size:9.5px;border-collapse:collapse}
.fhours td{height:18px;padding:0}
.fhours td:first-child{font-weight:700;width:81px}
.fhours-note{display:inline-block;margin-top:2px;font-size:9.5px;border-bottom:1px solid #aaa}
.faddr{font-size:10.5px;line-height:18px}
.frow{font-size:10.5px;display:flex;align-items:center;gap:7px;margin-top:7px}
.frow b{color:#555}
.frow span.link{color:var(--accent)}

.baseline{top:925px;left:151px;width:900px;border-top:1px solid #ddd}
.copy{top:942px;left:204px;font-size:9.5px;color:var(--text)}
.legal{top:940px;left:598px;font-size:10.5px;color:var(--accent);display:flex;gap:16px}
.foot-brand{top:936px;left:862px;display:flex;align-items:center;gap:8px;font-size:17px;font-weight:400;color:var(--faint)}
.foot-brand .mark{width:13px;height:13px;background:var(--faint)}
</style>
</head>
<body>

<div class="abs topbar">
  <span class="phone">
    <svg width="12" height="12" viewBox="0 0 12 12"><rect width="12" height="12" rx="2" fill="#555"/><path d="M3.3 2.6l1.4 1.4-.8 1a5 5 0 0 0 2.2 2.2l1-.8 1.4 1.4-.9 1.1C5.9 8.7 3.3 6.1 2.3 3.5z" fill="#fff"/></svg>
    804-555-0147
  </span>
  <a class="mail" href="#">name@tql.ab.ca</a>
  <nav class="links"><a href="#">Book an Appointment</a><a href="#">Physical Toolbox</a></nav>
</div>

<div class="abs card">
  <header class="header">
    <div class="brand">
      <div class="name"><span class="mark"></span>TQL Care Centre</div>
      <div class="tag">Trade Quality League Clinic</div>
    </div>
    <nav class="nav">
      <a href="#">Home</a><a class="current" href="#">Our Clinic</a><a href="#">Our Staff</a><a href="#">Resources</a><a href="#">Alerts</a><a href="#">Contact Us</a>
    </nav>
  </header>
</div>

<h1 class="abs title-band">Mission</h1>

<ul class="abs subnav">
  <li><span class="caret"><svg width="4" height="6"><path d="M0 0l4 3-4 3z" fill="#333"/></svg></span><span class="label">About</span></li>
  <li class="active"><span class="caret"><svg width="4" height="6"><path d="M0 0l4 3-4 3z" fill="#333"/></svg></span><span class="label">Mission</span></li>
  <li><span class="caret"><svg width="4" height="6"><path d="M0 0l4 3-4 3z" fill="#333"/></svg></span><span class="label">Services</span></li>
  <li><span class="caret"><svg width="4" height="6"><path d="M0 0l4 3-4 3z" fill="#333"/></svg></span><span class="label">Policies</span></li>
  <li><span class="caret"><svg width="4" height="6"><path d="M0 0l4 3-4 3z" fill="#333"/></svg></span><span class="label">Schedules</span></li>
</ul>

<section class="abs hero" role="img" aria-label="Clinic feature image area">
  <h2>WE TREAT PATIENTS LIKE HOME</h2>
  <a class="btn" href="#">Witness our Services Live</a>
</section>

<p class="abs lead">Sed consequat, leo eget bibendum sodales, augue velit cursus nunc, quis gravida magna mi a libero. Fusce vulputate eleifend</p>
<p class="abs body-copy" style="top:462px">Etiam sit amet orci eget eros faucibus tincidunt. Duis leo. Sed fringilla mauris sit<br>amet nibh. Donec sodales sagittis magna. Sed consequat, leo eget bibendum<br>sodales, augue velit cursus nunc, quis gravida magna mi a libero. Fusce vulpu-<br>tate eleifend sapien. Vestibulum purus quam, scelerisque ut, mollis sed,<br>nonummy id, metus.</p>
<p class="abs body-copy" style="top:570px">Etiam sit amet orci eget eros faucibus tincidunt. Duis leo. Sed fringilla mauris sit<br>amet nibh. Donec sodales sagittis magna. Sed consequat, leo eget bibendum<br>sodales, augue velit cursus nunc, quis gravida magna mi a libero. Fusce vulpu-<br>tate eleifend sapien. Vestibulum purus quam, scelerisque ut, mollis sed,</p>

<aside class="abs hours">
  <div class="head"><svg width="10" height="10" viewBox="0 0 10 10"><circle cx="5" cy="5" r="4" fill="none" stroke="#fff" stroke-width="1.4"/><path d="M5 2.6V5h1.8" fill="none" stroke="#fff" stroke-width="1.2"/></svg>Hours of Operation</div>
  <table>
    <tr><td>Monday</td><td>09:00 am - 4:00 pm</td></tr>
    <tr><td>Tuesday</td><td>05:00 am - 10:00 pm</td></tr>
    <tr><td>Wednesday</td><td>Not Available</td></tr>
    <tr><td>Thursday</td><td>09:00 am - 4:00 pm</td></tr>
    <tr><td>Friday</td><td>09:00 am - 4:00 pm</td></tr>
    <tr><td>Saturday</td><td>09:00 am - 4:00 pm</td></tr>
    <tr><td>Sunday</td><td>Not Available</td></tr>
  </table>
  <a class="holiday" href="#">Holiday Hours</a>
</aside>

<aside class="abs contact">
  <h3><svg width="12" height="12" viewBox="0 0 12 12"><path d="M2 1l2.2 2.2-1.1 1.4a6 6 0 0 0 4.3 4.3l1.4-1.1L11 10l-1.4 1.5C5.5 11 1 6.5.5 2.4z" fill="#1f3b45"/></svg>Contact Inquiries</h3>
  <dl>
    <dt>Telephone:</dt><dd>604-555-0182</dd>
    <dt>Email:</dt><dd>contact@cliniqo.ca</dd>
    <dt>Address:</dt><dd>48 Larchmont Avenue<br>Vancouver, B.C.<br>Canada, V5K 2R9</dd>
  </dl>
</aside>

<footer>
  <div class="abs fcol" style="left:204px">
    <h4>Our Clinic</h4>
    <ul class="flinks">
      <li class="on"><svg width="6" height="9"><path d="M1 1l4 3.5L1 8" fill="none" stroke="#555" stroke-width="1.6"/></svg>Mission</li>
      <li><svg width="6" height="9"><path d="M1 1l4 3.5L1 8" fill="none" stroke="#555" stroke-width="1.6"/></svg>Services</li>
      <li><svg width="6" height="9"><path d="M1 1l4 3.5L1 8" fill="none" stroke="#555" stroke-width="1.6"/></svg>Schedules</li>
      <li><svg width="6" height="9"><path d="M1 1l4 3.5L1 8" fill="none" stroke="#555" stroke-width="1.6"/></svg>Policies</li>
    </ul>
    <div class="fbig" style="margin-top:5px">STAFF<br>ALERTS<br>CONTACT US</div>
  </div>
  <div class="abs fcol" style="left:385px">
    <h4>Resources</h4>
    <ul class="flinks">
      <li class="on"><svg width="6" height="9"><path d="M1 1l4 3.5L1 8" fill="none" stroke="#555" stroke-width="1.6"/></svg>Our Clinic</li>
      <li><svg width="6" height="9"><path d="M1 1l4 3.5L1 8" fill="none" stroke="#555" stroke-width="1.6"/></svg>Mission</li>
      <li><svg width="6" height="9"><path d="M1 1l4 3.5L1 8" fill="none" stroke="#555" stroke-width="1.6"/></svg>Services</li>
      <li><svg width="6" height="9"><path d="M1 1l4 3.5L1 8" fill="none" stroke="#555" stroke-width="1.6"/></svg>Policies</li>
    </ul>
  </div>
  <div class="abs fcol" style="left:560px">
    <h4>Hours of Operation</h4>
    <table class="fhours">
      <tr><td>Monday</td><td>09:00 am - 4:00 pm</td></tr>
      <tr><td>Tuesday</td><td>05:00 am - 10:00 pm</td></tr>
      <tr><td>Wednesday</td><td>Not Available</td></tr>
      <tr><td>Thursday</td><td>09:00 am - 4:00 pm</td></tr>
      <tr><td>Friday</td><td>09:00 am - 4:00 pm</td></tr>
      <tr><td>Saturday</td><td>09:00 am - 4:00 pm</td></tr>
      <tr><td>Sunday</td><td>Not Available</td></tr>
    </table>
    <a class="fhours-note" href="#">Holiday Hours</a>
  </div>
  <div class="abs fcol" style="left:811px">
    <h4>Contact Us</h4>
    <p class="faddr">48 Larchmont Avenue. Vancouver, B.C.<br>Canada, V5K 2R9</p>
    <div class="frow" style="margin-top:11px"><svg width="9" height="9" viewBox="0 0 12 12"><path d="M2 1l2.2 2.2-1.1 1.4a6 6 0 0 0 4.3 4.3l1.4-1.1L11 10l-1.4 1.5C5.5 11 1 6.5.5 2.4z" fill="#555"/></svg><b>Phone</b> : 1604-555-0182</div>
    <div class="frow"><svg width="10" height="8" viewBox="0 0 10 8"><rect width="10" height="8" rx="1" fill="#555"/><path d="M0.5 1L5 4.5 9.5 1" fill="none" stroke="#fff"/></svg><b>Email</b> : <span class="link">info@tqlcare.ca</span></div>
    <div class="frow"><svg width="9" height="9" viewBox="0 0 10 10"><circle cx="5" cy="5" r="5" fill="#555"/><path d="M0 5h10M5 0c-2.5 3-2.5 7 0 10M5 0c2.5 3 2.5 7 0 10" fill="none" stroke="#fff" stroke-width=".8"/></svg><b>Website</b> : <span class="link">www.tqlcare.ca</span></div>
  </div>

  <div class="abs baseline"></div>
  <p class="abs copy">Copyright © 2015 TQL Care Centre Medical Healthcare Solutions. All Rights Reserved |</p>
  <nav class="abs legal"><a href="#">Terms</a><a href="#">Privacy Policy</a><a href="#">Legal Agreement</a></nav>
  <div class="abs foot-brand"><span class="mark"></span>TQL Care Centre</div>
</footer>

</body>
</html>
```